Change lives by changing education

We need stationery (business cards, letterhead, envelopes, with compliments slips and A4 display folders) that will support us to make an impact in education through recruitment and consultancy services. All our consultants are highly experienced with more than 20 years of industry experience and are all passionate about improving education by attracting the brightest and the best. We believe strongly in empowering students to take control of their own learning and turn their own ideas into reality.
We work in the independent/private school space which can be thought of as conservative, but they are just starting to "get with the times" and be more progressive, so the message has to carry across that space.We are a younger firm, but one of the few who has experienced educators running the show. Help us to make a difference to the world please!

Target Market(s)

Principals and School Board members

Industry/Entity Type

Business

Requirements
Must have
• The logo
Nice to have
• Use of the logo colours Indigo and a specific type of green
Should not have
• Nothing tacky to do with education, incl quills, pens, mortar boards, books

```html
<!DOCTYPE html>
<html lang="en">
<head>
<meta charset="UTF-8">
<title>Marlow Consulting – Business Card</title>
<link rel="stylesheet" href="https://fonts.googleapis.com/css2?family=Cinzel:wght@600&family=Open+Sans:wght@400&display=swap">
<style>
  :root {
    --backdrop: #3a3a3a;
    --card-white: #fbfbfb;
    --indigo: #2b2566;
    --green: #4c7a2e;
    --ink-grey: #555555;
    --white: #ffffff;
  }
  * { margin: 0; padding: 0; box-sizing: border-box; }
  html, body {
    width: 1200px; height: 750px; overflow: hidden;
    background: var(--backdrop);
  }
  .canvas { position: relative; width: 1200px; height: 750px; }

  .card {
    position: absolute; top: 228px;
    width: 461px; height: 262px; border-radius: 10px;
  }
  .card-front { left: 124px; background: var(--card-white); }
  .card-back  { left: 618px; background: var(--indigo); }

  .mark-area {
    position: absolute; left: 14px; top: 14px;
    width: 234px; height: 234px; border-radius: 50%;
    background: var(--indigo); opacity: 0.06;
  }

  .details {
    position: absolute; right: 25px; top: 26px;
    text-align: right; font-family: "Open Sans", sans-serif;
  }
  .person-name {
    font-family: "Cinzel", serif; font-weight: 600;
    font-size: 19px; letter-spacing: 1px; color: var(--indigo); line-height: 22px;
  }
  .person-role { font-size: 13px; color: var(--green); line-height: 16px; }
  .address { margin-top: 8px; font-size: 12px; color: var(--ink-grey); line-height: 15px; }
  .contact-list { list-style: none; margin-top: 8px; }
  .contact-list li {
    display: flex; justify-content: flex-end; align-items: center; gap: 7px;
    font-size: 12px; color: var(--ink-grey); line-height: 17.6px;
  }
  .contact-list svg { width: 11px; height: 11px; fill: var(--indigo); }

  .wordmark {
    font-family: "Cinzel", serif; font-weight: 600; color: var(--indigo);
    white-space: nowrap;
  }
  .card-front .wordmark {
    position: absolute; right: 25px; bottom: 34px; font-size: 22px;
  }
  .card-back .brand-lockup {
    position: absolute; left: 0; right: 0; top: 0; bottom: 0;
    display: flex; align-items: center; justify-content: center; gap: 14px;
  }
  .brand-dot { width: 40px; height: 40px; border-radius: 50%; background: var(--green); }
  .card-back .wordmark { color: var(--white); font-size: 28px; }
</style>
</head>
<body>
<main class="canvas">
  <section class="card card-front">
    <div class="mark-area" role="img" aria-label="Brand mark area"></div>
    <div class="details">
      <p class="person-name">Daniel Reeve</p>
      <p class="person-role">CEO/Founder</p>
      <p class="address">2140 Larchmont Road<br>Juneau, Alaska 99801</p>
      <ul class="contact-list">
        <li>907 512 4830
          <svg viewBox="0 0 24 24" aria-hidden="true"><path d="M6.6 10.8a15.1 15.1 0 0 0 6.6 6.6l2.2-2.2a1 1 0 0 1 1-.25 11.4 11.4 0 0 0 3.6.57 1 1 0 0 1 1 1V20a1 1 0 0 1-1 1A17 17 0 0 1 3 4a1 1 0 0 1 1-1h3.5a1 1 0 0 1 1 1c0 1.25.2 2.45.57 3.57a1 1 0 0 1-.25 1z"/></svg>
        </li>
        <li>907 388 2165
          <svg viewBox="0 0 24 24" aria-hidden="true"><path d="M7 1h10a2 2 0 0 1 2 2v18a2 2 0 0 1-2 2H7a2 2 0 0 1-2-2V3a2 2 0 0 1 2-2zm0 3v15h10V4z"/></svg>
        </li>
        <li>daniel@marlowedu.com
          <svg viewBox="0 0 24 24" aria-hidden="true"><path d="M2 5h20v14H2zm2 2v.5l8 5 8-5V7l-8 5z"/></svg>
        </li>
        <li>www.marlowedu.com
          <svg viewBox="0 0 24 24" aria-hidden="true"><path d="M12 2a10 10 0 1 0 0 20 10 10 0 0 0 0-20zm1 17.9V18a2 2 0 0 0-2-2v-2l-5-5-1.8.4A8 8 0 0 1 16 4.7V6a2 2 0 0 1-2 2h-2v2h4l3 3v3.5A8 8 0 0 1 13 19.9z"/></svg>
        </li>
      </ul>
    </div>
    <p class="wordmark">Marlow Consulting</p>
  </section>

  <section class="card card-back">
    <div class="brand-lockup">
      <span class="brand-dot" aria-hidden="true"></span>
      <p class="wordmark">Marlow Consulting</p>
    </div>
  </section>
</main>
</body>
</html>
```